New Business Card Design Project VORASTI-Italy

we are VORASTI-Italy
our company in the market for 3 years we are luxury cosmetic company and its about time for a facelift :)
i will like to have elegant luxurious and unique business card
that will give the person that get it a unique, luxurious and elegant impression
I'm VERY OPEN FOR NEW IDEAS , even duo i add a few files of things that i see on line and i like them

i add my logo as well
my website is VORASTI.COM
(if you would like to see the main style that we have)

Target Market(s)

adult that have money :)

Industry/Entity Type

Business

Contact Information for Business Card

Name - Paul Vorasti
Position - CEO and CO Founder
address - 4817 E Larkdale
telephone - 555-384-1962
email - paul@vorasti.com
fax - 555-384-1962
website - VORASTI.COM

Colors
000000
959595
fbee3e
ffffff

Requirements
Must have
• big logo in GOLD color
• elegant look
• impressive
Nice to have
• not must but maybe classy pattern background
• not must but maybe emblem
• maybe clear plastic business card
Should not have
• colors
• images

```html
<!DOCTYPE html>
<html lang="en">
<head>
<meta charset="utf-8">
<title>VORASTI Italy – Business Card</title>
<link rel="stylesheet" href="https://fonts.googleapis.com/css2?family=Cormorant+Garamond:wght@600&family=Josefin+Sans:wght@300;400&family=Roboto:wght@400&display=swap">
<style>
  :root {
    --gold: #e9aa3b;
    --card: #0c0c0c;
    --card-edge: #1b1b1b;
    --backdrop: #d9dde1;
    --ink: #0c0c0c;
  }
  * { box-sizing: border-box; margin: 0; padding: 0; }
  html, body { width: 1200px; height: 1200px; overflow: hidden; }
  body {
    background: var(--backdrop);
    position: relative;
    font-family: "Roboto", sans-serif;
  }
  .card {
    position: absolute;
    left: 150px;
    width: 900px;
    height: 514px;
    background: radial-gradient(ellipse at 50% 40%, var(--card-edge), var(--card) 70%);
    overflow: hidden;
    color: var(--gold);
  }
  .card--front { top: 70px; }
  .card--back { top: 616px; }

  /* Wordmark */
  .wordmark { font-family: "Cormorant Garamond", serif; font-weight: 600; color: var(--gold); }
  .wordmark__name { display: block; letter-spacing: 2px; line-height: 1; }
  .wordmark__rule { display: block; height: 4px; background: var(--gold); }
  .wordmark__region { display: block; text-align: center; letter-spacing: 3px; line-height: 1; }

  .card--front .seal {
    position: absolute; left: 380px; top: 60px;
    width: 140px; height: 140px; border-radius: 50%;
    border: 5px solid var(--gold);
  }
  .card--front .wordmark {
    position: absolute; left: 210px; top: 240px; width: 480px;
  }
  .card--front .wordmark__name { font-size: 118px; text-align: center; }
  .card--front .wordmark__rule { margin: 10px 0 14px; }
  .card--front .wordmark__region { font-size: 40px; }

  /* Back: contact side */
  .holder {
    position: absolute; left: 100px; top: 52px; width: 270px;
    font-family: "Josefin Sans", sans-serif; font-variant: small-caps;
  }
  .holder__name { font-size: 38px; font-weight: 300; letter-spacing: 1px; line-height: 1; }
  .holder__rule { height: 2px; background: var(--gold); margin: 8px 0 6px; }
  .holder__title { font-size: 15px; font-weight: 300; letter-spacing: 1px; text-align: center; }

  .contacts { position: absolute; left: 60px; top: 178px; list-style: none; }
  .contacts__item {
    display: flex; align-items: center; gap: 14px;
    height: 36px; margin-bottom: 22px;
    font-size: 23px; letter-spacing: 0.5px;
  }
  .contacts__icon { width: 34px; height: 34px; flex: none; }

  .divider {
    position: absolute; left: 430px; top: 30px;
    width: 3px; height: 420px; background: var(--gold);
  }
  .card--back .wordmark { position: absolute; left: 470px; top: 34px; width: 390px; }
  .card--back .wordmark__name { font-size: 90px; text-align: center; }
  .card--back .wordmark__rule { margin: 6px 0 10px; height: 3px; }
  .card--back .wordmark__region { font-size: 32px; }

  .card--back .seal {
    position: absolute; left: 580px; top: 230px;
    width: 440px; height: 440px; border-radius: 50%;
    border: 16px solid var(--gold);
  }
</style>
</head>
<body>

<section class="card card--front">
  <span class="seal"></span>
  <div class="wordmark">
    <span class="wordmark__name">VORASTI</span>
    <span class="wordmark__rule"></span>
    <span class="wordmark__region">ITALY</span>
  </div>
</section>

<section class="card card--back">
  <div class="holder">
    <p class="holder__name">Paul Vorasti</p>
    <div class="holder__rule"></div>
    <p class="holder__title">CEO and CO Founder</p>
  </div>

  <ul class="contacts">
    <li class="contacts__item">
      <svg class="contacts__icon" viewBox="0 0 34 34" aria-hidden="true">
        <rect width="34" height="34" rx="6" fill="var(--gold)"/>
        <path d="M17 6a8 8 0 0 0-8 8c0 6 8 14 8 14s8-8 8-14a8 8 0 0 0-8-8z" fill="var(--ink)"/>
        <circle cx="17" cy="14" r="3.2" fill="var(--gold)"/>
      </svg>
      <span>4817 E Larkdale</span>
    </li>
    <li class="contacts__item">
      <svg class="contacts__icon" viewBox="0 0 34 34" aria-hidden="true">
        <rect width="34" height="34" rx="6" fill="var(--gold)"/>
        <path d="M10 8l4-1 3 6-2.5 2a12 12 0 0 0 5.5 5.5l2-2.5 6 3-1 4c-9 1-18-8-17-17z" fill="var(--ink)"/>
      </svg>
      <span>555-384-1962</span>
    </li>
    <li class="contacts__item">
      <svg class="contacts__icon" viewBox="0 0 34 34" aria-hidden="true">
        <rect width="34" height="34" rx="6" fill="var(--gold)"/>
        <rect x="6" y="10" width="22" height="15" fill="none" stroke="var(--ink)" stroke-width="2"/>
        <path d="M6 10l11 9 11-9M6 25l8-7M28 25l-8-7" fill="none" stroke="var(--ink)" stroke-width="2"/>
      </svg>
      <span>paul@vorasti.com</span>
    </li>
    <li class="contacts__item">
      <svg class="contacts__icon" viewBox="0 0 34 34" aria-hidden="true">
        <rect width="34" height="34" rx="6" fill="var(--gold)"/>
        <rect x="11" y="6" width="12" height="8" fill="none" stroke="var(--ink)" stroke-width="2"/>
        <rect x="6" y="14" width="22" height="10" rx="2" fill="var(--ink)"/>
        <rect x="11" y="21" width="12" height="7" fill="var(--gold)" stroke="var(--ink)" stroke-width="2"/>
      </svg>
      <span>555-384-1962</span>
    </li>
    <li class="contacts__item">
      <svg class="contacts__icon" viewBox="0 0 34 34" aria-hidden="true">
        <rect width="34" height="34" rx="6" fill="var(--gold)"/>
        <circle cx="17" cy="17" r="10" fill="none" stroke="var(--ink)" stroke-width="2"/>
        <ellipse cx="17" cy="17" rx="4.5" ry="10" fill="none" stroke="var(--ink)" stroke-width="2"/>
        <path d="M7 17h20" stroke="var(--ink)" stroke-width="2"/>
      </svg>
      <span>vorasti.com</span>
    </li>
  </ul>

  <span class="divider"></span>

  <div class="wordmark">
    <span class="wordmark__name">VORASTI</span>
    <span class="wordmark__rule"></span>
    <span class="wordmark__region">ITALY</span>
  </div>

  <span class="seal"></span>
</section>

</body>
</html>
```